依頼詳細
バナーを見た人が気軽に専門書・学術書の買取に申し込むことができる、利用してみようと感じられるバナーをお願いします。
専門書・学術書を多く持つお客様(士業の方や大学教員など)が主なターゲットとなるため、落ち着いた・信頼感のある雰囲気のものを希望します。
記載項目
(1)「ミドリ書林ストア買取」もしくは「midori shorin store 買取」の文字とロゴ (ロゴは添付画像をご参照ください。)
(2)「専門書買取」の文字、もしくは専門書の買取に特化している、強いということを連想させる表記
(3)当店モットー「次の必要とする人へ繋ぎます」、もしくはそれに準じる表記
サイズ
• サイズは1200x628ピクセル、1200×1200、960×1200
希望イメージ
シンプル 複雑
単色 カラフル
暗い 明るい
日常 高級
遊び心 厳粛
未来的 伝統的
女性的 男性的
希望する色
茶系、上記イメージに沿うものであれば強いこだわりはございません。
納品ファイル
• 高解像度JPG (.jpg)
• イラストレーター形式 (.ai)
補足説明
最終的には異なるテイストの2作品を採用予定です。是非、奮ってご応募ください。

バナーという性質上で一番注意を引きそうなものを選ばせて頂きました。

いずれもクオリティの高い作品ばかりで悩みましたが2作品当選とさせて頂きました。
今回はご応募誠にありがとうございました。

```html
<!DOCTYPE html>
<html lang="ja">
<head>
<meta charset="UTF-8">
<title>ミドリ書林ストア買取 専門書買取バナー</title>
<link rel="stylesheet" href="https://fonts.googleapis.com/css2?family=Noto+Sans+JP:wght@500;700;900&display=swap">
<style>
  :root {
    --ink: #111111;
    --paper: #ffffff;
    --brand-brown: #7a5f2e;
    --book-red: #a3171c;
    --book-red-light: #b52228;
    --book-red-deep: #7d0f14;
    --page-edge: #ece6dc;
    --marble: #e6e4e1;
    --marble-light: #f4f3f1;
  }
  * { margin: 0; padding: 0; box-sizing: border-box; }
  html, body { width: 960px; height: 1200px; overflow: hidden; }
  body { font-family: "Noto Sans JP", sans-serif; background: var(--marble-light); }

  .banner { position: relative; width: 960px; height: 1200px; overflow: hidden; }

  .hero-photo {
    position: absolute; inset: 0;
    background: linear-gradient(160deg, var(--marble-light) 0%, var(--marble) 55%, var(--marble-light) 100%);
  }
  .hero-book {
    position: absolute; left: 136px; top: 140px;
    width: 632px; height: 912px;
    background: linear-gradient(150deg, var(--book-red-light) 0%, var(--book-red) 45%, var(--book-red-deep) 100%);
    border-radius: 4px 6px 6px 4px;
    box-shadow: 0 14px 30px rgba(0,0,0,0.22);
  }
  .hero-book::before {
    content: ""; position: absolute; left: 0; top: 0; bottom: 0; width: 16px;
    background: var(--book-red-deep); border-radius: 4px 0 0 4px;
  }
  .hero-book::after {
    content: ""; position: absolute; left: 40px; right: 0; bottom: -10px; height: 10px;
    background: var(--page-edge);
  }

  .brand-box {
    position: absolute; left: 21px; top: 19px;
    width: 162px; height: 190px;
    background: var(--paper);
    display: flex; flex-direction: column; align-items: center; justify-content: center;
    gap: 14px;
    box-shadow: 0 2px 6px rgba(0,0,0,0.12);
  }
  .brand-mark { width: 34px; height: 34px; background: var(--brand-brown); }
  .brand-name {
    font-weight: 700; font-size: 14px; line-height: 1.4;
    color: var(--brand-brown); text-align: center; letter-spacing: 0.02em;
  }

  .headline {
    position: absolute; right: 22px; top: 36px;
    writing-mode: vertical-rl;
    font-weight: 900; font-size: 104px; line-height: 1;
    color: var(--ink);
  }

  .motto {
    position: absolute; left: 436px; top: 256px;
    writing-mode: vertical-rl;
    font-weight: 700; font-size: 45px; line-height: 1;
    letter-spacing: 0.12em;
    color: var(--paper);
  }

  .cta {
    position: absolute; right: 0; bottom: 0;
    width: 353px; height: 53px;
    background: var(--ink); color: var(--paper);
    display: flex; align-items: center; justify-content: center; gap: 14px;
    font-weight: 700; font-size: 20px; letter-spacing: 0.06em;
    text-decoration: none;
  }
  .cta-arrow { width: 14px; height: 16px; }
</style>
</head>
<body>
  <div class="banner">
    <div class="hero-photo" role="img" aria-label="大理石のテーブルの上で、赤い布装の専門書を両手で次の人へ手渡している写真">
      <div class="hero-book"></div>
    </div>

    <div class="brand-box">
      <div class="brand-mark"></div>
      <p class="brand-name">midori shorin store<br>買取</p>
    </div>

    <h1 class="headline">専門書の買取に特化。</h1>

    <p class="motto">次の必要とする人へ繋ぎます。</p>

    <a class="cta" href="#">
      <svg class="cta-arrow" viewBox="0 0 14 16" aria-hidden="true"><polygon points="0,0 14,8 0,16" fill="#ffffff"/></svg>
      <span>詳しくはこちら</span>
    </a>
  </div>
</body>
</html>
```